Business Card Design.... Vantor logistics LLC --- Logo Included

Vantor logistics LLC is a small team trucking company....
Cards must match the website [login to view URL]
Red - Black - White

"Vantor Logistics"
"When Your Critical Freight Needs The Steady Hand Of A Seasoned Crew."

"Looking For A Reliable Team? Call To Hire Us!"

CONTEST WILL NOT LAST 5 DAYS!!!!!

```html
<!DOCTYPE html>
<html lang="en">
<head>
<meta charset="utf-8">
<title>Brennick Logistics LLC – Business Card</title>
<link rel="stylesheet" href="https://fonts.googleapis.com/css2?family=Poppins:wght@400;500;600;700&display=swap">
<style>
  :root {
    --red: #b3222a;
    --red-dark: #7d141a;
    --black: #141414;
    --white: #ffffff;
    --ink: #222222;
    --backdrop: #1f1f1f;
  }
  * { margin: 0; padding: 0; box-sizing: border-box; }
  html, body {
    width: 1200px;
    height: 780px;
    overflow: hidden;
    background: var(--backdrop);
    font-family: "Poppins", sans-serif;
  }
  .card-sheet {
    width: 1200px;
    height: 780px;
    display: flex;
    align-items: center;
    justify-content: center;
    gap: 40px;
  }
  .card {
    width: 560px;
    height: 320px;
    display: block;
    box-shadow: 0 10px 30px rgba(0, 0, 0, 0.5);
  }
  .card text { font-family: "Poppins", sans-serif; }
  .card-face { fill: var(--white); }
  .brand-mark { fill: var(--red); }
  .brand-name { fill: var(--ink); font-size: 19px; font-weight: 600; }
  .band-black { fill: var(--black); }
  .band-red { fill: var(--red); }
  .band-fold { fill: var(--red-dark); }
  .tagline { fill: var(--white); font-size: 11px; font-weight: 500; }
  .pitch { fill: var(--white); font-size: 16px; font-weight: 700; }
  .cta-pill { fill: var(--white); }
  .cta-label { fill: var(--red); font-size: 12px; font-weight: 700; }
  .contact-line { fill: var(--white); font-size: 12px; font-weight: 400; }
  .contact-icon { fill: none; stroke: var(--red); stroke-width: 1.8; stroke-linecap: round; stroke-linejoin: round; }
  .person-first { fill: var(--red); }
  .person-last { fill: var(--white); }
  .person-name { font-size: 19px; font-weight: 500; }
  .person-role { fill: var(--black); font-size: 13px; font-weight: 600; }
</style>
</head>
<body>
<main class="card-sheet">

  <svg class="card card-front" viewBox="0 0 560 320" aria-label="Business card front">
    <rect class="card-face" width="560" height="320"/>
    <g class="brand">
      <rect class="brand-mark" x="160" y="62" width="16" height="16"/>
      <text class="brand-name" x="184" y="77">Brennick Logistics LLC</text>
    </g>
    <polygon class="band-black" points="240,128 560,128 560,158 240,158"/>
    <polygon class="band-fold" points="290,148 300,158 290,158"/>
    <polygon class="band-red" points="0,148 290,148 290,262 0,272"/>
    <text class="tagline" x="20" y="170">When Your Critical Freight Needs</text>
    <text class="tagline" x="304" y="147">The Steady Hand Of A Seasoned Crew.</text>
    <text class="pitch" x="20" y="202">Looking For A</text>
    <text class="pitch" x="20" y="222">Reliable Team?</text>
    <rect class="cta-pill" x="20" y="232" width="124" height="24" rx="12"/>
    <text class="cta-label" x="82" y="248" text-anchor="middle">Call To Hire Us!</text>
  </svg>

  <svg class="card card-back" viewBox="0 0 560 320" aria-label="Business card back">
    <rect class="card-face" width="560" height="320"/>
    <g class="brand">
      <rect class="brand-mark" x="160" y="54" width="16" height="16"/>
      <text class="brand-name" x="184" y="69">Brennick Logistics LLC</text>
    </g>
    <polygon class="band-red" points="350,100 560,100 560,234 358,234"/>
    <polygon class="band-fold" points="358,234 368,234 362,246"/>
    <text class="contact-line" x="372" y="124">+01 555 0142 876</text>
    <text class="contact-line" x="372" y="139">+01 555 0198 321</text>
    <text class="contact-line" x="372" y="166">office@brennickmail.com</text>
    <text class="contact-line" x="372" y="181">www.brennickfreight.com</text>
    <text class="contact-line" x="372" y="210">48 Harbor Lane, Dayton, OH</text>

    <g class="contact-icons">
      <path class="contact-icon" d="M325,126 q0,-3 3,-3 l2,0 l1.5,4 l-2,1.5 q1.5,3 4.5,4.5 l1.5,-2 l4,1.5 l0,2 q0,3 -3,3 q-11,-1 -11.5,-11.5z"/>
      <circle class="contact-icon" cx="332" cy="172" r="6.5"/>
      <path class="contact-icon" d="M325.5,172 h13 M332,165.5 q-4,6.5 0,13 M332,165.5 q4,6.5 0,13"/>
      <path class="contact-icon" d="M332,214 q-6,-7 -6,-11 a6,6 0 0 1 12,0 q0,4 -6,11z"/>
      <circle class="contact-icon" cx="332" cy="203" r="2"/>
    </g>

    <polygon class="band-black" points="0,248 368,248 350,280 0,280"/>
    <text class="person-name" x="28" y="271"><tspan class="person-first">Daria</tspan><tspan class="person-last"> Holt</tspan></text>
    <text class="person-role" x="28" y="302">Manager</text>
  </svg>

</main>
</body>
</html>
```